Business card for marketing analytics company

Need a business card for new company. I have a logo already that I want to be built into the card and should use those colours

Company is called steered by tallies
Design must bring steered by tallies to life not be a card that could be for anyone with a logo put on it.

Like the front to be fairly clean and uncluttered bringing the logo out with a suitable design on the back of the card.

The logo represents a compass and business growth so those themes along with numbers, analytics , data are appropriate.
I'm often working with creative industries so also needs to reflect the creative side of analytics rather than be very corporate looking.

Target Market(s)

Ad agency, media agency, consumer goods clients

Industry/Entity Type

Market Research

Contact Information for Business Card

Needs to include name, title, email and phone number

Colors
f78f20
f68d4d
ec1f27

Requirements
Must have
• Must bring steered by tallies to life not be a card that could be for anyone with a logo put on it.
• Logo, Correct colours
• Like a design on the back that relates to company name
• Designs for both sides
Should not have
• Please do not just submit logo and a coloured card.
• It needs to have a design element to it
• No black background
• No clear cards - needs front & back

```html
<!DOCTYPE html>
<html lang="en">
<head>
<meta charset="utf-8">
<title>Steered by Tallies — Business Card</title>
<link href="https://fonts.googleapis.com/css2?family=Roboto:wght@400;500;700&display=swap" rel="stylesheet">
<style>
  :root {
    --backdrop: #dcdcdc;
    --card: #f7f7f7;
    --card-shade: #ececec;
    --ink-soft: #4a4f54;
    --grid: #d9d9d9;
    --brand-red: #a8221f;
    --brand-orange: #e0631c;
    --brand-amber: #f78f20;
  }
  html, body {
    margin: 0;
    padding: 0;
    width: 1200px;
    height: 576px;
    overflow: hidden;
    background: var(--backdrop);
    font-family: "Roboto", Arial, sans-serif;
  }
  .canvas { position: relative; width: 1200px; height: 576px; }
  .card {
    position: absolute;
    border-radius: 14px;
    background: linear-gradient(180deg, var(--card) 0%, var(--card-shade) 100%);
    box-shadow: 0 3px 6px rgba(0,0,0,0.18);
    overflow: hidden;
  }
  .card--front { left: 82px; top: 139px; width: 484px; height: 293px; }
  .card--back  { left: 602px; top: 138px; width: 481px; height: 291px; }

  /* Front */
  .front-brand {
    position: absolute;
    left: 0; right: 0; top: 0; bottom: 0;
    display: flex;
    align-items: center;
    justify-content: center;
    gap: 18px;
    margin-top: -12px;
  }
  .brand-dot {
    flex: none;
    width: 88px;
    height: 88px;
    border-radius: 50%;
    border: 3px solid var(--brand-orange);
    box-sizing: border-box;
  }
  .brand-name {
    font-weight: 500;
    font-size: 27px;
    line-height: 1;
    color: var(--brand-orange);
  }
  .front-tally {
    position: absolute;
    left: 0; right: 0; bottom: 0;
    height: 60px;
  }
  .front-tally svg { display: block; width: 100%; height: 100%; }

  /* Back */
  .accent-bar {
    position: absolute;
    left: 0; top: 36px;
    width: 13px; height: 48px;
    background: var(--brand-red);
  }
  .holder { position: absolute; left: 28px; top: 40px; }
  .holder__name {
    margin: 0;
    font-weight: 700;
    font-size: 18px;
    line-height: 22px;
    color: var(--brand-red);
  }
  .holder__title {
    margin: 2px 0 0;
    font-size: 11px;
    color: var(--ink-soft);
  }
  .back-brand {
    position: absolute;
    right: 24px;
    top: 34px;
    display: flex;
    flex-direction: column;
    align-items: center;
    gap: 6px;
  }
  .back-brand .brand-dot { width: 64px; height: 64px; }
  .back-brand .brand-name { font-size: 12px; }

  .growth-chart {
    position: absolute;
    right: 24px;
    bottom: 26px;
    width: 190px;
    height: 110px;
  }
  .growth-chart svg { display: block; width: 100%; height: 100%; }

  .contact-list {
    position: absolute;
    left: 33px;
    top: 216px;
    margin: 0; padding: 0;
    list-style: none;
  }
  .contact-list li {
    display: flex;
    align-items: center;
    gap: 9px;
    height: 17px;
    font-size: 12px;
    color: var(--ink-soft);
  }
  .contact-icon { width: 11px; height: 11px; flex: none; fill: var(--brand-orange); }
</style>
</head>
<body>
<main class="canvas">

  <section class="card card--front" aria-label="Card front">
    <div class="front-brand">
      <span class="brand-dot" aria-hidden="true"></span>
      <span class="brand-name">Steered by Tallies</span>
    </div>
    <div class="front-tally" aria-hidden="true">
      <svg viewBox="0 0 484 60" preserveAspectRatio="none">
        <g fill="var(--brand-amber)" opacity="0.35">
          <rect x="24" y="44" width="6" height="16"/>
          <rect x="36" y="38" width="6" height="22"/>
          <rect x="48" y="41" width="6" height="19"/>
          <rect x="60" y="32" width="6" height="28"/>
        </g>
        <g fill="var(--brand-red)" opacity="0.35">
          <rect x="424" y="40" width="6" height="20"/>
          <rect x="436" y="34" width="6" height="26"/>
          <rect x="448" y="28" width="6" height="32"/>
          <rect x="460" y="22" width="6" height="38"/>
        </g>
        <rect x="0" y="56" width="161" height="4" fill="var(--brand-amber)"/>
        <rect x="161" y="56" width="162" height="4" fill="var(--brand-orange)"/>
        <rect x="323" y="56" width="161" height="4" fill="var(--brand-red)"/>
      </svg>
    </div>
  </section>

  <section class="card card--back" aria-label="Card back">
    <div class="accent-bar" aria-hidden="true"></div>
    <div class="holder">
      <h1 class="holder__name">Mara T. Ellison</h1>
      <p class="holder__title">Managing Director</p>
    </div>

    <div class="back-brand">
      <span class="brand-dot" aria-hidden="true"></span>
      <span class="brand-name">Steered by Tallies</span>
    </div>

    <div class="growth-chart" aria-hidden="true">
      <svg viewBox="0 0 190 110">
        <g stroke="var(--grid)" stroke-width="1" stroke-dasharray="2 3">
          <line x1="0" y1="20" x2="190" y2="20"/>
          <line x1="0" y1="50" x2="190" y2="50"/>
          <line x1="0" y1="80" x2="190" y2="80"/>
        </g>
        <rect x="10"  y="82" width="18" height="26" fill="var(--brand-amber)"/>
        <rect x="40"  y="70" width="18" height="38" fill="var(--brand-amber)"/>
        <rect x="70"  y="76" width="18" height="32" fill="var(--brand-orange)"/>
        <rect x="100" y="56" width="18" height="52" fill="var(--brand-orange)"/>
        <rect x="130" y="40" width="18" height="68" fill="var(--brand-red)"/>
        <rect x="160" y="22" width="18" height="86" fill="var(--brand-red)"/>
        <line x1="0" y1="108.5" x2="190" y2="108.5" stroke="var(--ink-soft)" stroke-width="1"/>
      </svg>
    </div>

    <ul class="contact-list">
      <li>
        <svg class="contact-icon" viewBox="0 0 12 12" aria-hidden="true">
          <path d="M1 4.2C1 2.8 3 2 6 2s5 .8 5 2.2v1H8.6V4H3.4v1.2H1z"/>
          <path d="M2.5 6.2 4 4.8h4l1.5 1.4V10h-7z"/>
        </svg>
        <span>1300 418 418</span>
      </li>
      <li>
        <svg class="contact-icon" viewBox="0 0 12 12" aria-hidden="true">
          <circle cx="6" cy="6" r="5.3"/>
          <path d="M0.8 6h10.4M6 0.8c-2.2 2.8-2.2 7.6 0 10.4M6 0.8c2.2 2.8 2.2 7.6 0 10.4" stroke="#f3f3f3" stroke-width="0.9" fill="none"/>
        </svg>
        <span>www.sampledomain.com</span>
      </li>
      <li>
        <svg class="contact-icon" viewBox="0 0 12 12" aria-hidden="true">
          <rect x="0.5" y="2.5" width="11" height="7.5"/>
          <path d="M0.8 2.8 6 7l5.2-4.2" stroke="#f3f3f3" stroke-width="0.9" fill="none"/>
        </svg>
        <span>mara.ellison@sampledomain.com</span>
      </li>
    </ul>
  </section>

</main>
</body>
</html>
```